Certificate Design for Employee Loyalty

We're a digital marketing agency in Australia (www.brightkitestudio.com.au) and we're looking to create a design for a certificate to celebrate employees who reach 5 years with us (we have a few coming up soon).
Ideally we'd want something that captures our funky, digital agency culture (see our Facebook page www.facebook.com/brightkitestudio for what we mean) and not be too "corporatey"
A4 portrait or landscape designs would be awesome, with spots for employee's name, a brief 2-3 line message and a design that reflects our culture and the 5 year milestone for the employee.
Any questions, please post!
Target Market(s)
Digital marketing employees.

```html
<!DOCTYPE html>
<html lang="en">
<head>
<meta charset="utf-8">
<title>Certificate of Appreciation – Bright Kite Studio</title>
<link rel="stylesheet" href="https://fonts.googleapis.com/css2?family=Pinyon+Script&family=Great+Vibes&family=Oswald:wght@500&display=swap">
<style>
  :root {
    --backdrop: #5a3a2a;
    --paper-light: #f8dc95;
    --paper-mid: #e7b45a;
    --paper-edge: #c4842c;
    --paper-border: #f4efe6;
    --script-red: #a8392d;
    --bar-red: #a5332b;
    --label-blue: #2c4e7c;
    --ink: #1b1410;
    --badge-black: #0b0b0b;
    --badge-text: #f2f2f2;
  }
  * { margin: 0; padding: 0; box-sizing: border-box; }
  html, body { width: 1200px; height: 875px; overflow: hidden; }
  body { background: var(--backdrop); position: relative; }

  .certificate {
    position: absolute;
    left: 92px; top: 66px;
    width: 1016px; height: 740px;
    background: radial-gradient(ellipse at 48% 45%, var(--paper-light) 0%, var(--paper-mid) 55%, var(--paper-edge) 100%);
    border: 2px dashed var(--paper-border);
    outline: 1px solid var(--paper-border);
  }

  .message {
    position: absolute;
    left: 285px; top: 146px;
    width: 420px;
    text-align: center;
    font-family: "Pinyon Script", cursive;
    font-weight: 400;
    font-size: 40px;
    line-height: 50.5px;
    color: var(--script-red);
  }
  .message span { display: block; white-space: nowrap; }

  .studio-badge {
    position: absolute;
    left: 758px; top: 143px;
    width: 167px; height: 167px;
    background: var(--badge-black);
    display: flex; align-items: center; justify-content: center;
    text-align: center;
    font-family: "Oswald", sans-serif;
    font-weight: 500;
    font-size: 22px;
    line-height: 1.15;
    letter-spacing: 1px;
    color: var(--badge-text);
  }

  .signatures { position: absolute; left: 0; top: 0; width: 100%; height: 100%; }
  .sign-bar {
    position: absolute;
    left: 53px; top: 634px;
    width: 925px; height: 20px;
    background: var(--bar-red);
  }
  .signer { position: absolute; top: 576px; }
  .signer .name {
    display: block;
    font-family: "Pinyon Script", cursive;
    font-size: 38px;
    line-height: 60px;
    color: var(--ink);
    white-space: nowrap;
  }
  .signer .role {
    position: absolute;
    top: 82px;
    font-family: "Oswald", sans-serif;
    font-weight: 500;
    font-size: 19px;
    letter-spacing: 1.2px;
    color: var(--label-blue);
    white-space: nowrap;
  }
  .signer--president { left: 56px; }
  .signer--president .role { left: -2px; }
  .signer--awardee { left: 0; width: 1016px; text-align: center; }
  .signer--awardee .name { font-family: "Great Vibes", cursive; font-size: 40px; font-weight: 700; -webkit-text-stroke: 0.6px var(--ink); }
  .signer--awardee .role { left: 0; width: 100%; text-align: center; }
  .signer--secretary { right: 40px; text-align: right; }
  .signer--secretary .role { right: 8px; }
</style>
</head>
<body>
  <main class="certificate">
    <h1 class="message">
      <span>Certificate</span>
      <span>of Appreciation</span>
      <span>From Bright Kite Studio</span>
      <span>To Thank You For</span>
      <span>Your Five Years</span>
      <span>of Dedicated</span>
      <span>Service</span>
    </h1>

    <div class="studio-badge">Bright Kite<br>Studio</div>

    <section class="signatures">
      <div class="sign-bar"></div>
      <div class="signer signer--president">
        <span class="name">Milo Hart</span>
        <span class="role">PRESIDENT</span>
      </div>
      <div class="signer signer--awardee">
        <span class="name">Jonah Reyes</span>
        <span class="role">AWARDEE</span>
      </div>
      <div class="signer signer--secretary">
        <span class="name">Wren Hart</span>
        <span class="role">SECRETARY</span>
      </div>
    </section>
  </main>
</body>
</html>
```